Business Card Design

We develop / design / build affordable housing throughout the state of Illinois.

Target Market(s)

non profit organizations and other developers / professionals in my industry

Industry/Entity Type

Business

Contact Information for Business Card

Brightmoor Construction, LLC
General Contracting
Rosalind K Tavener, CEO
482 North Wendell Ashby Avenue, Suite 310
Elmhurst, IL 60126
630-555-0147
rkt@buildbrightmoor.com

```html
<!DOCTYPE html>
<html lang="en">
<head>
<meta charset="utf-8">
<title>Brightmoor Construction – Business Card</title>
<link href="https://fonts.googleapis.com/css2?family=Open+Sans:ital,wght@0,400;0,700;1,400&display=swap" rel="stylesheet">
<style>
  :root {
    --backdrop: #424244;
    --brand-red: #be1e2d;
    --accent-red: #e0403a;
    --paper: #ffffff;
    --ink-gray: #5a5a5c;
    --rule-gray: #8a8a8c;
  }
  * { margin: 0; padding: 0; box-sizing: border-box; }
  html, body { width: 1200px; height: 1000px; overflow: hidden; }
  body {
    background: var(--backdrop);
    font-family: "Open Sans", Arial, sans-serif;
    position: relative;
  }
  .card {
    position: absolute;
    left: 286px;
    width: 621px;
    height: 364px;
  }
  .card--front { top: 95px; background: var(--brand-red); }
  .card--back { top: 541px; background: var(--paper); }

  .front-mark {
    position: absolute;
    left: 50%;
    top: 140px;
    width: 56px;
    height: 56px;
    margin-left: -28px;
    background: var(--paper);
  }
  .front-name {
    position: absolute;
    left: 0;
    right: 0;
    top: 256px;
    text-align: center;
    color: var(--paper);
    font-weight: 700;
    font-size: 20px;
    letter-spacing: 0.2px;
  }

  .back-brand {
    position: absolute;
    left: 93px;
    top: 120px;
    width: 118px;
    text-align: center;
  }
  .back-brand__square {
    display: block;
    width: 44px;
    height: 44px;
    margin: 0 auto 14px;
    background: var(--brand-red);
  }
  .back-brand__name {
    color: var(--brand-red);
    font-weight: 700;
    font-size: 17px;
  }
  .divider {
    position: absolute;
    left: 254px;
    top: 116px;
    width: 1px;
    height: 158px;
    background: var(--rule-gray);
  }
  .contact {
    position: absolute;
    left: 283px;
    top: 106px;
  }
  .contact__name {
    color: var(--brand-red);
    font-weight: 700;
    font-size: 23px;
    line-height: 32px;
  }
  .contact__title {
    color: var(--accent-red);
    font-style: italic;
    font-size: 20px;
    line-height: 34px;
    margin-bottom: 8px;
  }
  .contact__line {
    color: var(--ink-gray);
    font-size: 17.5px;
    line-height: 23px;
  }
</style>
</head>
<body>
  <section class="card card--front">
    <span class="front-mark"></span>
    <p class="front-name">Brightmoor Construction</p>
  </section>

  <section class="card card--back">
    <div class="back-brand">
      <span class="back-brand__square"></span>
      <span class="back-brand__name">Brightmoor</span>
    </div>
    <span class="divider"></span>
    <div class="contact">
      <h1 class="contact__name">Rosalind K. Tavener</h1>
      <p class="contact__title">CEO</p>
      <p class="contact__line">482 North Wendell Ashby Avenue,</p>
      <p class="contact__line">Suite 310 Elmhurst, IL 60126</p>
      <p class="contact__line">630-555-0147</p>
      <p class="contact__line">rkt@buildbrightmoor.com</p>
    </div>
  </section>
</body>
</html>
```